Construction business card

I need a new business card, they can connect with my logo, brand.
What we do is residential house , design and build
I like: Navy blue / black
I attached our logo, brand,
and, some idea for business card.

```html
<!DOCTYPE html>
<html lang="en">
<head>
<meta charset="utf-8">
<title>Ridgeline Building Group – Business Card</title>
<link href="https://fonts.googleapis.com/css2?family=Poppins:wght@400;500;700&display=swap" rel="stylesheet">
<style>
  :root {
    --backdrop: #b1b2b1;
    --card-blue: #317bc2;
    --card-blue-deep: #2a6fb3;
    --ink-white: #ffffff;
    --ink-black: #111111;
  }
  * { box-sizing: border-box; margin: 0; padding: 0; }
  html, body { width: 1200px; height: 939px; overflow: hidden; }
  body {
    background: var(--backdrop);
    font-family: "Poppins", sans-serif;
    position: relative;
  }
  .card {
    position: absolute;
    width: 500px;
    height: 286px;
    background: var(--card-blue);
    color: var(--ink-white);
    box-shadow: 0 6px 14px rgba(0,0,0,0.25);
  }
  .card--front { left: 80px; top: 150px; }
  .card--back  { left: 620px; top: 500px; }

  .brand {
    position: absolute;
    left: 50%; top: 50%;
    transform: translate(-50%, -50%);
    display: flex;
    align-items: center;
    gap: 12px;
    white-space: nowrap;
  }
  .brand__square {
    width: 26px; height: 26px;
    background: var(--ink-black);
  }
  .brand__name {
    font-weight: 700;
    font-size: 22px;
    letter-spacing: 0.5px;
    color: var(--ink-white);
    text-transform: uppercase;
  }

  .contact {
    position: absolute;
    left: 34px; top: 56px;
    font-size: 12px;
    line-height: 1.55;
  }
  .contact__name {
    font-weight: 700;
    font-size: 19px;
    text-transform: uppercase;
    line-height: 1.2;
  }
  .contact__role { font-size: 14px; margin-bottom: 2px; }
  .contact__line { display: flex; align-items: center; gap: 7px; }
  .contact__line svg { width: 12px; height: 12px; flex: none; }

  .brand-faint {
    position: absolute;
    right: 26px; top: 34px;
    font-weight: 700;
    font-size: 18px;
    line-height: 1.1;
    text-transform: uppercase;
    color: var(--card-blue-deep);
    text-align: right;
  }
</style>
</head>
<body>

  <section class="card card--front">
    <div class="brand">
      <span class="brand__square"></span>
      <span class="brand__name">Ridgeline Building Group</span>
    </div>
  </section>

  <section class="card card--back">
    <div class="brand-faint">Ridgeline<br>Building Group</div>
    <div class="contact">
      <p class="contact__name">Daniel Hoang Tran</p>
      <p class="contact__role">Director</p>
      <p>RIDGELINE BUILDING GROUP PTY LTD</p>
      <p>ABN: 00 123 456 789</p>
      <p class="contact__line">
        <svg viewBox="0 0 12 12"><rect x="3" y="0.5" width="6" height="11" rx="1" fill="none" stroke="#fff" stroke-width="1.3"/><rect x="4.5" y="2" width="3" height="6" fill="#fff"/></svg>
        0400 555 218
      </p>
      <p class="contact__line">
        <svg viewBox="0 0 12 12"><rect x="0.5" y="2" width="11" height="8" fill="#fff"/><path d="M0.5 2 L6 7 L11.5 2" fill="none" stroke="#317bc2" stroke-width="1.2"/></svg>
        info@ridgelinebuild.com.au
      </p>
      <p class="contact__line">
        <svg viewBox="0 0 12 12"><path d="M6 11.5 C2 7 2 5.5 2 4.5 A4 4 0 0 1 10 4.5 C10 5.5 10 7 6 11.5Z" fill="#fff"/><circle cx="6" cy="4.5" r="1.5" fill="#317bc2"/></svg>
        42 Harbour Lane, Springvale, VIC 3171
      </p>
      <p class="contact__line">
        <svg viewBox="0 0 12 12" fill="none" stroke="#fff" stroke-width="1"><circle cx="6" cy="6" r="5"/><ellipse cx="6" cy="6" rx="2.2" ry="5"/><path d="M1 6 H11 M2 3.5 H10 M2 8.5 H10"/></svg>
        www.ridgelinebuild.com.au
      </p>
    </div>
  </section>

</body>
</html>
```